Stylish new business card needed!

Hello everyone! I am in need of a new business card design for an alarm company here in Hurricane WV. I have all fonts, color codes and logos provided for you use! We are a young company and like the style of a clean sleek looking business card. Would like it double sided, one side holding the logo and the other with your design!
Target Market(s)
The people that are looking for the newest tech for home automation and security
Industry/Entity Type
Alarm services; Home automation
Contact Information for Business Card
Name of person; position (Sales; Installer); Phone Number (555.419.7362); Employee cell Number; Website (www.GuardedByVelm.example); Employee Email; Double sided
Look and feel
Each slider illustrates characteristics of the customer's brand and the style your logo design should communicate.

```html
<!DOCTYPE html>
<html lang="en">
<head>
<meta charset="utf-8">
<title>Velm Business Card</title>
<link href="https://fonts.googleapis.com/css2?family=Montserrat:wght@500;800&display=swap" rel="stylesheet">
<style>
  :root {
    --stage: #e0e0e0;
    --card-light: #ffffff;
    --card-dark: #000000;
    --grey: #999999;
    --orange: #fc8f4c;
    --orange-soft: rgba(252, 143, 76, 0.16);
    --dark-accent: #1e1e1e;
  }
  * { margin: 0; padding: 0; box-sizing: border-box; }
  html, body {
    width: 1200px; height: 1200px; overflow: hidden;
    background: var(--stage);
    font-family: "Montserrat", Arial, sans-serif;
  }
  .card {
    position: absolute; left: 294px; width: 612px; height: 349px; overflow: hidden;
  }
  .card--front { top: 228px; background: var(--card-light); }
  .card--back { top: 622px; background: var(--card-dark); }
  .card__accent { position: absolute; left: 0; top: 0; }

  .brand { position: absolute; display: flex; align-items: center; color: var(--grey); font-weight: 500; line-height: 1; letter-spacing: 2px; }
  .brand__dot { border-radius: 50%; background: var(--orange); margin-right: 12px; }
  .card--front .brand { left: 33px; top: 40px; font-size: 74px; }
  .card--front .brand__dot { width: 22px; height: 22px; }

  .contact { position: absolute; left: 33px; top: 176px; color: var(--grey); font-size: 16.5px; font-weight: 500; line-height: 20.5px; }
  .contact__gap { height: 20px; }

  .tagline-top { position: absolute; left: 90px; top: 98px; color: var(--orange); font-weight: 800; font-size: 23px; letter-spacing: 1.5px; }
  .card--back .brand { left: 64px; top: 134px; font-size: 96px; }
  .card--back .brand__dot { width: 28px; height: 28px; }
  .tagline-bottom { position: absolute; left: 84px; top: 237px; color: var(--orange); font-weight: 800; font-size: 9.6px; letter-spacing: 0.6px; }
</style>
</head>
<body>
  <section class="card card--front">
    <svg class="card__accent" width="612" height="349" viewBox="0 0 612 349" aria-hidden="true">
      <circle cx="590" cy="300" r="210" fill="var(--orange-soft)"/>
    </svg>
    <div class="brand"><span class="brand__dot"></span>VELM</div>
    <div class="contact">
      <p>Name of Person</p>
      <p>Position (Sales; Installer)</p>
      <div class="contact__gap"></div>
      <p>Phone: (555.419.7362)</p>
      <p>Employee Cell: (000000000)</p>
      <p>Website: www.GuardedByVelm.example</p>
      <p>Employee Email: info@velm.example</p>
    </div>
  </section>

  <section class="card card--back">
    <svg class="card__accent" width="612" height="349" viewBox="0 0 612 349" aria-hidden="true">
      <circle cx="590" cy="300" r="210" fill="var(--dark-accent)"/>
    </svg>
    <p class="tagline-top">PROTECTED BY</p>
    <div class="brand"><span class="brand__dot"></span>VELM</div>
    <p class="tagline-bottom">AUTOMATION AND SECURITY SERVICES</p>
  </section>
</body>
</html>
```